Redesign of LumaWireHub.com website

Revised description:
We would like to redesign our 8 year old website (in Pagecraft) to something fresh and current. Although I've attached our log, we are open to a new logo if you have a cool idea but it should have lumawirehub.com somewhere in the logo.  We are going to eventually put 5 rotating images on the homepage but for the interest of this design contest, I would like you to use  just one image (#23), only on the small laptop screen in the image, I would like to see the lumawirehub homepage inserted (that you've designed) giving the illusion that whoever was using that laptop was looking at the lumawirehub website. The tagline "your high-end equipment deserves high-end cables." should be somewhere on the image as well.
This is an open slate, we are open to new colors, designs, etc. We really want something simple, not crowded with images, etc.
I have included a bunch of pictures to use or you can use your own. You can use the same product categories that we currently have on the website. There should also be a place on the homepage to insert our Vidstream video.
We sell to businesses and get a lot of orders from the government and military so the site should be catered towards this market. We sell very little to consumers. Our biggest competitor is q7v.com but we don't really want something that looks like their site. Something closer to a tobe.com or kp.com is more what we're looking for. Please keep in mind that we also want people to know its a retail site, where they can purchase cables. The winner of this will likely have additional $$ work as we will be making a lot of product changes in the near future.

Target Market(s)
We sell fiber optic and copper cables to Government agencies, military, colleges/universities, small & large businesses. Mostly male. 25-50.
Industry/Entity Type
Government
Requirements
Must have
- We are different from our competition in the following ways:
1. FREE ground shipping on ALL orders
2. We build custom cables in the USA
3. We have a lifetime warranty on ALL of our cables so we use the highest quality components
4. We are on the west coast so we have up to 3 extra hours to ship our product for same day shipping
5. We stock over 100,000 different cables
6. Our prices are competitive
You can watch our Vidstream video to get an idea : )
Nice to have
- I've included a lot of images below for inspiration or to use on the site when appropriate.
Here is a site that I really like. You need to cut and paste it.
http://layoutbazaar.example/item/velora-site-theme-a-shop-theme/full_screen_preview/774310
Should not have
- Anything "cartoony" or whimsical.

```html
<!DOCTYPE html>
<html lang="en">
<head>
<meta charset="utf-8">
<title>LumaWireHub.com — Home</title>
<link rel="stylesheet" href="https://fonts.googleapis.com/css2?family=Open+Sans:wght@400;600;700&family=Roboto+Condensed:wght@700&display=swap">
<style>
:root{
  --green:#6f9a3f;
  --green-dark:#5a8232;
  --orange:#f27a1a;
  --ink:#2f2f2f;
  --muted:#666;
  --line:#e3e3e3;
  --panel:#f1f1f1;
  --footer:#1f1f1f;
  --footer-text:#cfcfcf;
  --white:#fff;
}
*{box-sizing:border-box;margin:0;padding:0}
html,body{width:667px;height:1200px;overflow:hidden;background:var(--white)}
body{position:relative;font-family:"Open Sans",Arial,sans-serif;color:var(--ink);font-size:7px}
.abs{position:absolute}

/* header */
.brand{left:72px;top:20px;display:flex;align-items:center;gap:5px;width:140px;white-space:nowrap}
.brand-dot{width:16px;height:16px;border-radius:50%;background:var(--orange);flex:none}
.brand-name{font-size:13px;font-weight:700;color:var(--green);letter-spacing:-.3px}
.search-label{left:225px;top:24px;font-size:7px;color:#999;line-height:1}
.search-label b{display:block;font-size:12px;color:#999;font-weight:600}
.search-box{left:269px;top:23px;width:214px;height:20px;border:1px solid #ddd;border-radius:2px;padding:4px 6px;color:#aaa;font-size:7.5px}
.search-go{left:460px;top:25px;width:20px;height:16px;border-radius:8px;background:#d9d9d9;color:#fff;font-size:7px;text-align:center;line-height:16px}
.account{right:74px;top:9px;font-size:6.5px;color:#888;word-spacing:2px}
.cart{right:74px;top:29px;font-size:6.5px;color:#888}
.cart b{color:var(--green);font-weight:600}
.nav{left:225px;top:52px;width:369px;height:21px;background:var(--green);display:flex;align-items:center;white-space:nowrap}
.nav a{color:var(--white);font-size:8px;text-decoration:none;padding:0 8px;border-right:1px solid rgba(255,255,255,.35);line-height:21px}
.nav-free{margin-left:auto;display:flex;align-items:center;gap:4px;color:#fff;font-size:7.5px;line-height:1;padding-right:8px;text-align:center}
.nav-free b{background:var(--orange);padding:4px 5px;font-size:10px;font-weight:700}

/* hero */
.hero{left:0;top:77px;width:667px;height:260px;background:linear-gradient(100deg,#f4f4f4 0%,#d9dcdf 35%,#3d4350 62%,#1d2230 100%)}
.hero-tag{left:72px;top:170px;font-family:"Roboto Condensed",Arial,sans-serif;font-weight:700;line-height:.95;text-transform:uppercase;white-space:nowrap}
.hero-tag .l1{font-size:17px;color:#2b2b2b}
.hero-tag .l2{font-size:30px;color:var(--orange)}
.hero-tag .l3{font-size:34px;color:var(--green)}

/* sidebar */
.cat-head{left:73px;top:364px;width:117px;height:21px;background:var(--orange);color:#fff;font-weight:700;font-size:12px;padding:3px 7px;border-radius:2px 2px 0 0}
.cat-list{left:73px;top:386px;width:117px;background:var(--panel);list-style:none;padding-bottom:4px}
.cat-list li{font-size:6px;color:#444;padding:4px 9px;border-bottom:1px solid #e2e2e2;height:15.1px;line-height:7px;white-space:nowrap;overflow:hidden}
.news{left:73px;top:710px;width:117px;height:130px;background:var(--panel)}
.news-small{position:absolute;left:0;top:1px;font-size:8px;color:#555;background:#fff;width:117px;padding-bottom:1px}
.news-big{position:absolute;left:0;top:10px;font-size:12.5px;font-weight:700;color:#333;background:#fff;width:117px;padding-bottom:4px;border-bottom:1px solid #ccc}
.news-copy{position:absolute;left:5px;top:32px;width:110px;font-size:6.5px;line-height:10px;color:#555}
.news-field{position:absolute;left:6px;top:73px;width:106px;height:18px;background:#fff;border:1px solid #ddd;font-size:7px;color:#777;text-align:center;line-height:16px}
.news-btn{position:absolute;left:30px;top:99px;width:58px;height:20px;background:var(--orange);color:#fff;font-weight:700;font-size:8.5px;text-align:center;line-height:20px;border-radius:2px}
.promo{left:73px;width:118px;height:46px;color:#fff;font-size:7px;font-weight:700;padding:11px 5px;line-height:12px;border-radius:2px}
.promo.gov{top:856px;background:linear-gradient(#89b257,var(--green-dark))}
.promo.edu{top:917px;background:linear-gradient(#f99640,#e56d0d)}
.promo svg{position:absolute;right:8px;bottom:8px}

/* features */
.feat{width:111px;height:106px;border:1px solid var(--line);background:#fff}
.feat-head{height:35px;background:var(--green);color:#fff;font-weight:700;font-size:8px;line-height:10px;padding:7px 10px}
.feat-art{margin:14px auto 0;width:62px;height:40px;border-radius:3px}
.feat-center{left:335px;top:492px;width:134px;text-align:center;font-size:7.3px;line-height:12px}
.feat-center b{display:block;font-weight:700;color:#222;margin-bottom:6px}
.feat-center span{color:#555}
.video-btn{left:382px;top:573px;width:43px;height:28px;background:#111}
.rule{left:211px;width:382px;height:1px;background:var(--line)}

/* intro copy */
.h2{left:211px;font-size:11.5px;font-weight:700;color:#222;letter-spacing:.2px;white-space:nowrap}
.intro{width:176px;font-size:7px;line-height:12px;color:#555}
.intro b{display:block;color:#222;font-weight:600;margin-bottom:8px}
.slider-nav{left:578px;top:805px;width:16px;height:10px;border:1px solid #ccc}

/* products */
.product{width:118px;height:180px;padding:0 10px}
.product.active{border:1px solid var(--line);box-shadow:0 0 3px rgba(0,0,0,.08)}
.product-art{width:100px;height:75px;margin-top:5px;border-radius:2px}
.product h3{font-size:7px;font-weight:600;color:#222;margin-top:21px;white-space:nowrap}
.product p{font-size:6.4px;color:#777;line-height:11px;margin-top:8px;height:22px;overflow:hidden}
.product .buy{display:flex;justify-content:space-between;align-items:center;margin-top:20px}
.price{font-size:8px;font-weight:700;color:#222}
.cart-btn{background:var(--green);color:#fff;font-size:6.5px;padding:3px 6px;border-radius:2px}

/* footer */
.footer{left:0;top:1053px;width:667px;height:147px;background:var(--footer);color:var(--footer-text);font-size:6.8px}
.foot-brand{position:absolute;left:72px;top:28px;display:flex;align-items:center;gap:5px;white-space:nowrap}
.foot-brand .brand-dot{width:14px;height:14px}
.foot-brand .brand-name{font-size:12.5px}
.copy{position:absolute;left:72px;top:78px;width:120px;line-height:11px}
.pay{position:absolute;left:72px;top:110px;display:flex;gap:3px}
.pay i{display:block;width:19px;height:12px;background:#e8e8e8;border-radius:1px}
.col{position:absolute;top:22px}
.col h4{font-size:7.5px;font-weight:600;color:#fff;margin-bottom:12px}
.col li{list-style:none;line-height:14.5px}
.contact-row{display:flex;gap:7px;line-height:10.5px;margin-bottom:10px}
.contact-row svg{flex:none;margin-top:1px}
.social{display:flex;gap:4px;margin-bottom:12px}
.social i{display:block;width:15px;height:15px;border-radius:50%;background:#e8e8e8}
</style>
</head>
<body>

<header>
  <div class="abs brand"><span class="brand-dot"></span><span class="brand-name">lumawirehub.com</span></div>
  <div class="abs search-label">SEARCH BY<b>DEVICE</b></div>
  <div class="abs search-box">Enter Keywords</div>
  <div class="abs search-go">Go</div>
  <div class="abs account">MY ACCOUNT &nbsp;| &nbsp;CHECK OUT &nbsp;| &nbsp;LOGIN</div>
  <div class="abs cart">SHOPPING CART <b>&#128722; $0.00</b></div>
  <nav class="abs nav">
    <a>HOME</a><a>ABOUT US</a><a>GOV/EDU BUYERS</a><a>RESELLERS</a><a style="border:none">CONTACT</a>
    <div class="nav-free"><b>FREE</b><span>And Fast<br>Delivery</span></div>
  </nav>
</header>

<section class="abs hero" role="img" aria-label="Server room aisle with a rack-mounted laptop console showing the store homepage">
  <svg class="abs" style="left:20px;top:107px" width="26" height="50" viewBox="0 0 26 50"><path d="M24 2 2 25l22 23" fill="none" stroke="#fff" stroke-width="2"/></svg>
  <svg class="abs" style="left:621px;top:107px" width="26" height="50" viewBox="0 0 26 50"><path d="M2 2l22 23L2 48" fill="none" stroke="#fff" stroke-width="2"/></svg>
</section>
<h1 class="abs hero-tag"><div class="l1">Your high-end equipment</div><div class="l2">Deserves high</div><div class="l3">End cables</div></h1>

<aside>
  <div class="abs cat-head">CATEGORY</div>
  <ul class="abs cat-list">
    <li style="color:#222">HOME</li><li>10 Gig 50/125 Multimode Cables</li><li>62.5/125 Multimode Cables</li><li>50/125 Multimode Cables</li><li>9/125 Singlemode Cables</li><li>PLENUM Fiber Cables</li><li>Mode Conditioning Cables</li><li>GBIC/Transceivers/SFP</li><li>Attenuators</li><li>Fiber Pigtails - 900 Micron</li><li>Fiber Media Converters</li><li>Fiber Couplers</li><li>Cat5e Patch Cables</li><li>Cat6 Patch Cables</li><li>CAT6A Patch Cables</li><li>Component Video RGB Cables</li><li>HDMI Cables</li><li>Cat6 Cables - Made in the U.S.A.</li><li>Custom Colors - Fiber</li><li>Contact Us</li>
  </ul>
  <div class="abs news">
    <div class="news-small">SIGNUP TO OUR</div>
    <div class="news-big">NEWSLETTER</div>
    <p class="news-copy">Enter your email address below to sign up to our newsletter and receive all our latest specials</p>
    <div class="news-field">Your Email Address</div>
    <div class="news-btn">SIGN UP</div>
  </div>
  <div class="abs promo gov">GOVERNMENT MILITARY<br>PREFERRED PRICING
    <svg width="18" height="16" viewBox="0 0 18 16"><path d="M1 5 9 1l8 4zM2 14h14v2H2zM3 6h2v7H3zm4 0h2v7H7zm4 0h2v7h-2z" fill="#fff"/></svg></div>
  <div class="abs promo edu">EDUCATIONAL INSTITUTION<br>PREFERRED PRICING
    <svg width="20" height="16" viewBox="0 0 20 16"><path d="M10 3C7 1 4 1 1 2v13c3-1 6-1 9 1 3-2 6-2 9-1V2c-3-1-6-1-9 1zm0 0v13" fill="none" stroke="#fff" stroke-width="1.6"/></svg></div>
</aside>

<main>
  <div class="abs feat" style="left:212px;top:365px"><div class="feat-head">We build custom cables in the USA</div><div class="feat-art" role="img" aria-label="Map of the United States in flag colours" style="background:linear-gradient(#c8102e 0 33%,#f2f2f2 33% 66%,#2a3f8f 66%)"></div></div>
  <div class="abs feat" style="left:347px;top:365px"><div class="feat-head">Free ground shipping on ALL orders</div><div class="feat-art" role="img" aria-label="Hand truck carrying a shipping box" style="background:linear-gradient(#c98a4a,#8a5a2c);width:40px"></div></div>
  <div class="abs feat" style="left:482px;top:365px"><div class="feat-head">We stock over 100,000 different cables</div><div class="feat-art" role="img" aria-label="Bundle of colourful fiber strands" style="background:linear-gradient(120deg,#222,#555 50%,#4aa3d8)"></div></div>

  <div class="abs feat" style="left:212px;top:495px"><div class="feat-head" style="padding-top:12px">Lifetime Warranty</div><div class="feat-art" role="img" aria-label="Gold warranty seal" style="background:radial-gradient(#f5c842,#d49a10);width:42px;height:42px;border-radius:50%"></div></div>
  <div class="abs feat-center"><b>We are on the west coast so we have up to 3 extra hours to ship our product for same day Shipping</b><span>You can watch our<br>Vidstream video to get an idea</span></div>
  <div class="abs video-btn"><svg width="43" height="28" viewBox="0 0 43 28"><circle cx="21.5" cy="14" r="9" fill="none" stroke="#fff" stroke-width="2"/><path d="M19 9.5l7 4.5-7 4.5z" fill="#fff"/></svg></div>
  <div class="abs feat" style="left:482px;top:495px"><div class="feat-head">Our prices are competitive</div><div class="feat-art" role="img" aria-label="Wallet with banknotes and a gold coin" style="background:linear-gradient(135deg,#2b2b2b,#3d6b3a 60%,#d8a829)"></div></div>

  <div class="abs rule" style="top:626px"></div>
  <h2 class="abs h2" style="top:651px">FIBER OPTIC CABLES</h2>
  <div class="abs intro" style="left:211px;top:671px"><b>Our new TAA compliant and Made in the U.S.A cables are ideal for government contracts.</b>We can build TAA compliant copper patch cords in Cat5e, Cat6 and Cat6a. Our popular custom fiber line can be manufactured in Indoor/Outdoor, Armored, Aerial, Direct Burial and many others.</div>
  <div class="abs intro" style="left:412px;top:671px"><b>Are you looking for a custom length that is not provided on our website?</b>Send us us a quick email or call us at 555-210-7784 and we'll post it on the website for you. We want to make it as easy as possible for you to get the exact length that you want. Not only do we stock over 75,000 pre-made fiber assemblies, but we can build almost any custom fiber cable you can imagine.</div>

  <h2 class="abs h2" style="top:800px">WHAT'S NEW AT LUMAWIREHUB</h2>
  <div class="abs slider-nav"><svg width="16" height="10" viewBox="0 0 16 10"><path d="M6 2 3 5l3 3M10 2l3 3-3 3" fill="none" stroke="#999"/><path d="M8 0v10" stroke="#ccc"/></svg></div>
  <div class="abs rule" style="top:821px"></div>

  <article class="abs product active" style="left:212px;top:842px">
    <div class="product-art" role="img" aria-label="Yellow singlemode fiber patch cable with connectors" style="background:linear-gradient(135deg,#f3d23a,#e8e8e8 55%,#222)"></div>
    <h3>Lifetime Warranty</h3><p>Converts Singlemode and Multimode fiber ...</p>
    <div class="buy"><span class="price">$150.00</span><span class="cart-btn">Add to Cart</span></div>
  </article>
  <article class="abs product" style="left:343px;top:842px">
    <div class="product-art" role="img" aria-label="Blue duplex multimode fiber cable" style="background:linear-gradient(135deg,#2c47c8,#dcdcdc 60%,#2c47c8)"></div>
    <h3>Multimode Duplex 62.5/125</h3><p>Multimode Duplex PVC 62.5/125 Keldar Optical Fiber...</p>
    <div class="buy"><span class="price">$150.00</span><span class="cart-btn">Add to Cart</span></div>
  </article>
  <article class="abs product" style="left:474px;top:842px">
    <div class="product-art" role="img" aria-label="Orange multimode SC-SC fiber jumper" style="background:linear-gradient(135deg,#f07a2a,#e2dcd2 60%,#c9b9a5)"></div>
    <h3>Fiber jumper SC-SC</h3><p>Orange Multimode Duplex Keldar optical fiber....</p>
    <div class="buy"><span class="price">$150.00</span><span class="cart-btn">Add to Cart</span></div>
  </article>
</main>

<footer class="abs footer">
  <div class="foot-brand"><span class="brand-dot"></span><span class="brand-name">lumawirehub.com</span></div>
  <p class="copy">Copyright © 2014 LumaWireHub.com All Right reserved.</p>
  <div class="pay"><i></i><i></i><i></i><i></i><i></i></div>

  <div class="col" style="left:230px"><h4>Contact Info</h4>
    <div class="contact-row"><svg width="7" height="9" viewBox="0 0 7 9"><path d="M3.5 0A3.3 3.3 0 0 0 .2 3.3C.2 5.8 3.5 9 3.5 9s3.3-3.2 3.3-5.7A3.3 3.3 0 0 0 3.5 0zm0 4.6a1.3 1.3 0 1 1 0-2.6 1.3 1.3 0 0 1 0 2.6z" fill="#aaa"/></svg><span>48 Calle Verano, Mesa<br>Linda, CA 90417</span></div>
    <div class="contact-row"><svg width="8" height="8" viewBox="0 0 8 8"><path d="M1.6.3 3 1.9 2.3 3a4.6 4.6 0 0 0 2.7 2.7L6.1 5l1.6 1.4-.9 1.3C3.6 7.6.4 4.4.3 1.2z" fill="#aaa"/></svg><span>Phone:<br>(555) 210-7784</span></div>
    <div class="contact-row"><svg width="8" height="6" viewBox="0 0 8 6"><rect x=".5" y=".5" width="7" height="5" fill="none" stroke="#aaa"/><path d="M.5.5 4 3.5 7.5.5" fill="none" stroke="#aaa"/></svg><span>E-mail:<br>info@lumawirehub.com</span></div>
  </div>
  <div class="col" style="left:411px"><h4>Quick links</h4>
    <ul><li>About Us</li><li>Questions/FAQ</li><li>Contact Us</li><li>Return Policy</li><li>Promotions</li></ul></div>
  <div class="col" style="left:522px"><h4>Follow Us</h4>
    <div class="social"><i></i><i></i><i></i><i></i></div>
    <ul><li>Promotion Terms</li><li>Referral Program</li><li>Fiber Tutorial</li></ul></div>
</footer>

</body>
</html>
```